Halvern Properties Business Cards

I would like a business card that includes myself and my partner.
Includes: Logo, office #, email, website, our names, our numbers and possibly the address. I would also like the logo to be embossed and the card to be horizontal.
There is a photo of our yard signs to give you an idea of the colors of our business.

Target Market(s)

Everyone in real estate market.
We are in a rural area. Our clientele are from all socioeconomic backgrounds.

Industry/Entity Type

Real Estate Agent

Contact Information for Business Card

Company Name: Halvern Properties
Our Names, Titles & Cell #'s : Marla Halvern-Broker (555).316.4827, Tessa Halvern-Realtor (555).627.9154
Office #: (555).841.2600
Website: halvernproperties-example.com
Joint Email: halvern@halvernproperties-example.com
Office Address: 518B W. Cottonwell Ave.
Wrenford, XX. 70999

Font styles to use
Serif

Requirements
Must have
• HORIZONTAL, Logo, Myself and my partners names, Our cell #'s, our office #, our website, our email address
Nice to have
• Embossed logo, office address, our titles.

```html
<!DOCTYPE html>
<html lang="en">
<head>
<meta charset="utf-8">
<title>Halvern Properties Business Cards</title>
<link rel="stylesheet" href="https://fonts.googleapis.com/css2?family=Crimson+Pro:wght@600&family=Open+Sans:wght@400;600&display=swap">
<style>
  :root {
    --purple: #46195f;
    --purple-deep: #4a1f6a;
    --purple-glow: #9b72ba;
    --ink: #2b2b2b;
    --rule: #b8adc4;
    --white: #ffffff;
    --stage-top: #a3a3a3;
    --stage-bottom: #858585;
  }
  * { margin: 0; padding: 0; box-sizing: border-box; }
  html, body { width: 1200px; height: 900px; overflow: hidden; }
  body {
    background: linear-gradient(180deg, var(--stage-top), var(--stage-bottom));
    font-family: "Open Sans", Arial, sans-serif;
    color: var(--ink);
    position: relative;
  }
  .card {
    position: absolute;
    top: 306px;
    width: 439px;
    height: 271px;
    border-radius: 12px;
    box-shadow: 0 1px 3px rgba(0,0,0,0.25);
    overflow: hidden;
  }
  .card-front { left: 149px; background: var(--white); }
  .card-back {
    left: 608px;
    background: radial-gradient(ellipse 58% 62% at 50% 48%, var(--purple-glow) 0%, #7a4d9c 45%, var(--purple-deep) 100%);
  }
  .wordmark {
    position: absolute;
    left: 0; right: 0;
    display: flex;
    align-items: center;
    justify-content: center;
    gap: 10px;
    font-family: "Crimson Pro", Georgia, serif;
    font-weight: 600;
    font-size: 31px;
    letter-spacing: 0.3px;
    line-height: 1;
  }
  .wordmark-dot { width: 22px; height: 22px; border-radius: 50%; }
  .card-front .wordmark { top: 48px; color: var(--purple); }
  .card-front .wordmark-dot { background: var(--purple); }
  .card-back .wordmark { top: 119px; color: var(--white); }
  .card-back .wordmark-dot { background: var(--white); }

  .agent { position: absolute; top: 124px; font-size: 12px; line-height: 1.3; }
  .agent-name { font-weight: 600; font-size: 14px; color: var(--purple); }
  .agent-title { font-size: 11.5px; }
  .agent-phone { margin-top: 3px; display: flex; align-items: center; gap: 5px; font-size: 12px; }
  .agent-left { right: 235px; text-align: right; }
  .agent-left .agent-phone { justify-content: flex-end; }
  .agent-right { left: 226px; text-align: left; }
  .agent-right .agent-phone { flex-direction: row-reverse; justify-content: flex-end; }

  .office { position: absolute; left: 0; right: 0; font-size: 12px; display: flex; justify-content: center; gap: 8px; line-height: 1.3; }
  .office-row-1 { top: 189px; }
  .office-row-2 { top: 205px; }
  .office-item { display: flex; align-items: center; gap: 4px; }
  .icon { width: 10px; height: 10px; fill: var(--purple); flex: none; }

  .address {
    position: absolute; top: 232px; left: 0; right: 0;
    display: flex; align-items: center; gap: 10px; font-size: 11.5px;
  }
  .address::before, .address::after { content: ""; flex: 1; height: 1px; background: var(--rule); }
</style>
</head>
<body>
  <section class="card card-front" aria-label="Business card front">
    <div class="wordmark"><span class="wordmark-dot"></span>Halvern Properties</div>

    <div class="agent agent-left">
      <div class="agent-name">Marla Halvern</div>
      <div class="agent-title">Broker</div>
      <div class="agent-phone">(555).316.4827
        <svg class="icon" viewBox="0 0 10 10"><path d="M2 0.5l1.6 2.2-1 1a6 6 0 0 0 3.7 3.7l1-1L9.5 8 8.3 9.5C4.3 9.3.7 5.7.5 1.7z"/></svg>
      </div>
    </div>
    <div class="agent agent-right">
      <div class="agent-name">Tessa Halvern</div>
      <div class="agent-title">Realtor</div>
      <div class="agent-phone">(555).627.9154
        <svg class="icon" viewBox="0 0 10 10"><path d="M2 0.5l1.6 2.2-1 1a6 6 0 0 0 3.7 3.7l1-1L9.5 8 8.3 9.5C4.3 9.3.7 5.7.5 1.7z"/></svg>
      </div>
    </div>

    <div class="office office-row-1">
      <span class="office-item">
        <svg class="icon" viewBox="0 0 10 10"><path d="M2 0.5l1.6 2.2-1 1a6 6 0 0 0 3.7 3.7l1-1L9.5 8 8.3 9.5C4.3 9.3.7 5.7.5 1.7z"/></svg>(555).841.2600
      </span>
      <span class="office-item">
        <svg class="icon" viewBox="0 0 10 10"><path d="M0.5 2h9v6h-9z M0.5 2l4.5 3.5L9.5 2" stroke="#fff" stroke-width="0.8"/></svg>halvern@halvernproperties-example.com
      </span>
    </div>
    <div class="office office-row-2">
      <span class="office-item">
        <svg class="icon" viewBox="0 0 10 10"><circle cx="5" cy="5" r="4.5"/><path d="M0.5 5h9M5 0.5c2 2.5 2 6.5 0 9M5 0.5c-2 2.5-2 6.5 0 9" stroke="#fff" stroke-width="0.7" fill="none"/></svg>halvernproperties-example.com
      </span>
    </div>

    <div class="address">518B W. Cottonwell Ave. Wrenford, XX. 70999</div>
  </section>

  <section class="card card-back" aria-label="Business card back">
    <div class="wordmark"><span class="wordmark-dot"></span>Halvern Properties</div>
  </section>
</body>
</html>
```